Create a Landing Page Design

I need a landing page designed and coded in HTML for tallfern.com that follows an "F" pattern design.

Examples:

Quillbarrow: https://www.quillbarrow.example/form/sem/sales_software.jsp?d=48260000000tkP7&DCMP=KNC-Search&mkwid=R8wq2Lm5&pcrid=58204917362&type=Exact&pdv=c&nc=48260000000mbHQ&gclid=DKoRn47f2M1DGfSmPhpeRHxBkR
Jug: https://app.jug.example/signup/o/sendlargefiles?kw=jug%20cloud%20storage&gclid=DJaLrfnf2M1DGT2fPhpe1GNBOR
Cobaltwick: http://www.cobaltwick.example/Landing-Templates/Search-Demo/?Reach_Campaign_ID=48270000000Jtwu&Reach_Campaign_Status=Registered&LeadSource=OnlineDemo_Search_48270000000Jtwu&PromoCode=OnlineDemo_Search_48270000000Jtwu&gclid=DJD1pL7g2M1DGZziPhpePH5B6R
Plumtide: http://pages2.plumtide.example/PPC-MarketingAutomationforLife.html?source=PPC&comment=PPC_GS_US&ag=Competition%20-%20Norvane&camp=Competition%20Marketing%20Automation&_kk=52542849458&kw=norvane&gclid=DMzSmKPg2M1DGX6fPhpeQycBLB
Gladwell Helper: http://gladwellhelper.example/free-helpdesk-software?gclid=DKQFovjg2M1DGfxEPhpegNB1h
Pult: http://help.pult.example/free-trial?source1=Adverts-CPC-Freetrial-BramlineNA&pi_ad_id=59602686359&gclid=DQ_ftf3g2M1DGf18PhpeilJBvB

It needs:

- Bullet point content to the left
- Sign-up form to the right (with image) - we'll provide the code for this
- Testimonials underneath
- A "human" image that conveys that there are people behind the brand. Here's a link to a filecrate folder of stock images we've purchased on this theme: https://www.filecrate.example/sh/uz1fbp5upmj0nvy/q5hL7VVvl8

I've attached a simple SketchRill wireframe so you understand what we're looking for.

We'd like to use our existing (https://tallfern.com/) header and footer, but remove all links (other than privacy policy + terms of service).

Thanks!

```html
<!DOCTYPE html>
<html lang="en">
<head>
<meta charset="utf-8">
<title>Tallfern – Free Membership</title>
<link href="https://fonts.googleapis.com/css2?family=Mulish:ital,wght@0,400;0,500;0,600;0,800;1,400&family=Open+Sans:ital,wght@0,400;1,400&family=Noto+Serif:wght@400&display=swap" rel="stylesheet">
<style>
  :root{
    --ink:#333;
    --grey:#6b6b6b;
    --muted:#a8a8a8;
    --teal:#1c8fb0;
    --teal-band:#2694b5;
    --teal-text:#2a96b8;
    --green:#7db53c;
    --green-dark:#5c9420;
    --red:#d92f45;
    --field:#efefef;
    --field-line:#d3d3d3;
    --frame:#e6e6e6;
    --footer:#2f2d32;
    --footer-text:#7a7a7a;
  }
  *{box-sizing:border-box;margin:0;padding:0}
  html,body{width:1200px;height:1100px;overflow:hidden;background:#fff}
  body{position:relative;font-family:"Mulish",sans-serif;color:var(--ink)}
  .top-rule{position:absolute;left:0;top:0;width:1200px;height:7px;background:#262626}

  .brand{position:absolute;left:100px;top:5px;display:flex;align-items:center;z-index:3}
  .brand-mark{width:130px;height:130px;border-radius:50%;background:var(--teal)}
  .brand-name{margin-left:28px;font-size:52px;font-weight:500;color:#6a6a6a;letter-spacing:-0.5px}

  .hero{position:absolute;left:0;top:115px;width:1200px;height:328px;
    background:linear-gradient(180deg,#3aa2c0 0%,#2c97b7 55%,#2590b1 100%)}
  .hero-title{position:absolute;left:99px;top:318px;font-size:47px;font-weight:500;color:#fff;letter-spacing:0.2px}
  .hero-sub{position:absolute;left:101px;top:372px;font-size:20px;color:#fff}

  .signup{position:absolute;left:719px;top:77px;width:381px;height:409px;background:#fff;
    border:3px solid var(--frame);padding:24px 17px 0 16px;z-index:2}
  .signup-shadow{position:absolute;left:745px;top:482px;width:330px;height:22px;
    background:radial-gradient(ellipse at 50% 0%,rgba(0,0,0,.28),rgba(0,0,0,0) 70%)}
  .signup h2{font-family:"Open Sans",sans-serif;font-style:italic;font-weight:400;font-size:19px;color:var(--teal-text)}
  .signup p{font-family:"Open Sans",sans-serif;font-style:italic;font-size:13px;line-height:22px;color:#555;margin-top:8px;letter-spacing:-0.2px}
  .field{position:relative;width:300px;height:43px;margin:24px 0 0 4px;background:var(--field);
    border:1px solid var(--field-line);border-radius:2px}
  .field + .field{margin-top:7px}
  .field input{width:100%;height:100%;border:0;background:transparent;padding:0 19px;
    font-family:"Mulish",sans-serif;font-size:14px;color:#888}
  .field input::placeholder{color:#8a8a8a}
  .field svg{position:absolute;right:18px;top:14px}
  .choices{margin:16px 0 0 12px;font-size:14px;color:#666;letter-spacing:.3px}
  .choices label{display:flex;align-items:center;height:21px}
  .choices .dot{width:13px;height:13px;border-radius:50%;border:1px solid #4d8fc0;
    background:radial-gradient(#fff,#dbe8f2);margin-right:11px}
  .submit{display:block;margin:22px 0 0 88px;width:147px;height:38px;border-radius:19px;border:1px solid #4e8a1a;
    background:linear-gradient(#8cc43e,#5c9820);color:#fff;font-family:"Mulish",sans-serif;font-size:18px;font-weight:600;letter-spacing:.6px}

  .benefits{position:absolute;left:101px;top:485px;width:560px}
  .benefit{position:absolute;left:0;display:flex}
  .benefit .badge{width:51px;height:51px;border-radius:50%;flex:none;display:flex;align-items:center;justify-content:center}
  .benefit h3{font-size:22px;font-weight:400;color:#444;margin:1px 0 0 17px;white-space:nowrap}
  .benefit p{font-family:"Noto Serif",serif;font-size:11px;line-height:18px;color:#444;margin:3px 0 0 18px;width:455px}

  .testimonial{position:absolute;left:721px;width:360px}
  .avatar{position:absolute;left:0;top:0;width:61px;height:61px;border-radius:50%;
    background:radial-gradient(circle,#d9d9d9,#b9b9b9);border:2px solid #eee}
  .testimonial blockquote{position:absolute;left:77px;top:2px;width:282px;font-family:"Open Sans",sans-serif;font-style:italic;
    font-size:15px;line-height:22px;color:var(--muted)}
  .testimonial cite{position:absolute;left:78px;top:76px;font-family:"Open Sans",sans-serif;font-style:italic;font-size:15px;color:var(--teal-text);white-space:nowrap}

  .partners{position:absolute;left:200px;top:844px;width:800px;height:40px;display:flex;align-items:center;color:#8c8c8c}
  .partners span{position:absolute;font-size:22px;white-space:nowrap}

  .footer{position:absolute;left:0;top:908px;width:1200px;height:192px;background:var(--footer)}
  .footer h4{position:absolute;left:104px;top:22px;font-size:22px;font-weight:800;color:#5a5a5c}
  .social{position:absolute;left:104px;top:68px;display:flex;gap:4px}
  .social span{width:50px;height:50px;border-radius:50%}
  .footer-rule{position:absolute;left:105px;top:140px;width:680px;height:1px;background:#4a484d}
  .legal{position:absolute;left:106px;top:156px;font-family:"Open Sans",sans-serif;font-size:12px;color:var(--footer-text)}
  .legal a{color:var(--footer-text)}
  .footer-brand{position:absolute;left:811px;top:122px;display:flex;align-items:center}
  .footer-brand .mark{width:46px;height:46px;border-radius:50%;background:#e0872b}
  .footer-brand span{margin-left:12px;font-size:30px;font-weight:500;color:#8a8a8a}
</style>
</head>
<body>
  <div class="top-rule"></div>

  <section class="hero" role="img" aria-label="Group photo of smiling people standing together, tinted teal"></section>
  <header class="brand">
    <div class="brand-mark"></div>
    <div class="brand-name">Tallfern</div>
  </header>
  <h1 class="hero-title">Promising An End Benefit</h1>
  <div class="hero-sub">Summarizing How to get it</div>

  <div class="signup-shadow"></div>
  <form class="signup">
    <h2>Free Membership</h2>
    <p>Join the growing number of people who have discovered the power and ease of Tallfern.</p>
    <div class="field"><input type="text" placeholder="First Name *">
      <svg width="14" height="14" viewBox="0 0 14 14"><circle cx="7" cy="4" r="3.5" fill="#999"/><path d="M0 14c0-4 3-6 7-6s7 2 7 6z" fill="#999"/></svg></div>
    <div class="field"><input type="text" placeholder="Last Name *">
      <svg width="14" height="14" viewBox="0 0 14 14"><circle cx="7" cy="4" r="3.5" fill="#999"/><path d="M0 14c0-4 3-6 7-6s7 2 7 6z" fill="#999"/></svg></div>
    <div class="field"><input type="email" placeholder="E-mail *">
      <svg width="17" height="13" viewBox="0 0 17 13"><rect width="17" height="13" fill="#999"/><path d="M1 1l7.5 6L16 1M1 12l5-5M16 12l-5-5" stroke="#efefef" stroke-width="1.3" fill="none"/></svg></div>
    <div class="choices">
      <label><span class="dot"></span>I want to hire a freelancer</label>
      <label><span class="dot"></span>I am a freelancer</label>
    </div>
    <button class="submit" type="button">Submit</button>
  </form>

  <section class="benefits">
    <div class="benefit" style="top:0">
      <div class="badge" style="background:var(--green)">
        <svg width="30" height="26" viewBox="0 0 30 26" fill="none" stroke="#fff" stroke-width="2"><rect x="2" y="4" width="24" height="15"/><path d="M10 24h10M15 19v5M11 14l12-12"/></svg>
      </div>
      <div><h3>Sed do eaiusmod tempor incididunt proident</h3>
        <p>Duis aute irure dolor in reprehenderit in voluptate velit esse cillum dolore eu fugiat nulla pariatur. Excepteur sint occaecat cupidatat non proident.</p></div>
    </div>
    <div class="benefit" style="top:100px">
      <div class="badge" style="background:var(--teal)">
        <svg width="30" height="24" viewBox="0 0 30 24" fill="none" stroke="#fff" stroke-width="2"><rect x="2" y="2" width="26" height="20"/><path d="M2 7h26"/><text x="15" y="18" fill="#fff" stroke="none" font-size="9" text-anchor="middle" font-family="sans-serif">&lt;/&gt;</text></svg>
      </div>
      <div><h3>Sed do eiusmod tempor incididunt ut proident</h3>
        <p>Duis aute irure dolor in reprehenderit in voluptate velit esse cillum dolore eu fugiat nulla pariatur. Excepteur sint.</p></div>
    </div>
    <div class="benefit" style="top:205px">
      <div class="badge" style="background:var(--red)">
        <svg width="30" height="26" viewBox="0 0 30 26" fill="none" stroke="#fff" stroke-width="2"><rect x="2" y="2" width="26" height="22"/><path d="M2 7h26"/><path d="M12 11l7 4.5-7 4.5z" fill="#fff"/></svg>
      </div>
      <div><h3>Sed do eiusmod tempor incididunt proident</h3>
        <p>Duis aute irure dolor in reprehenderit in voluptate velit esse cillum dolore eu fugiat nulla pariatur. Excepteur sint occaecat cupidatat non proident, sunt in culpa qui officia deserunt mollit anim id est laborum.</p></div>
    </div>
  </section>

  <figure class="testimonial" style="top:531px">
    <div class="avatar" role="img" aria-label="Portrait photo of the customer"></div>
    <blockquote>Duis aute irure dolor in reprehenderit in velit esse cillum dolore eu fugiat nulla pariatur.</blockquote>
    <cite>Dorian Vellacott</cite>
  </figure>
  <figure class="testimonial" style="top:662px">
    <div class="avatar" role="img" aria-label="Portrait photo of the customer"></div>
    <blockquote>Duis aute irure dolor in reprehenderit in velit esse cillum dolore eu fugiat nulla pariatur.</blockquote>
    <cite>Dorian Vellacott</cite>
  </figure>

  <div class="partners">
    <span style="left:0">Brindle</span>
    <span style="left:152px">Haverly 365</span>
    <span style="left:304px">Search Kite</span>
    <span style="left:486px">Tindral</span>
    <span style="left:686px">Slatewing</span>
  </div>

  <footer class="footer">
    <h4>Connect with us</h4>
    <div class="social" aria-label="Social links">
      <span style="background:#4a6aa8"></span>
      <span style="background:#5bb8e0"></span>
      <span style="background:#4b4b4b"></span>
      <span style="background:#1a7fc0"></span>
    </div>
    <div class="footer-rule"></div>
    <p class="legal">Copyright © 2014 Tallfern, Inc. Larkspur Bay, CA | All Rights Reserved | <a href="#">Terms and Conditions</a> | <a href="#">Privacy Policy</a></p>
    <div class="footer-brand"><div class="mark"></div><span>Tallfern</span></div>
  </footer>
</body>
</html>
```